Make attractive Packaging label for NUT BUTTERS jars

We at Velvet Orchard are launching our own line of NUT BUTTERS. We will be serving them in GLASS JARS ready packaged. I need attractive luxurious design for glass jar and should be designed ready to print.
I have attached glass jar pictures and measurement sheet.
My company logo has been attached. Also company details can be found on our facebook page.
product will be

ALMOND BUTTER
CASHEW BUTTER
PEANUT BUTTER
HAZELNUT BUTTER.

```html
<!DOCTYPE html>
<html lang="en">
<head>
<meta charset="utf-8">
<title>Velvet Orchard – Almond Butter Label</title>
<link href="https://fonts.googleapis.com/css2?family=Montserrat:wght@400;800&display=swap" rel="stylesheet">
<style>
  :root {
    --page: #ffffff;
    --brown-dark: #2f1a0c;
    --brown: #4f2e15;
    --gold-dark: #a8691f;
    --gold: #c98a35;
    --gold-light: #dcb05a;
    --silver-light: #f6f6f6;
    --silver: #e4e4e4;
    --ink: #1e1e1e;
    --white: #ffffff;
    --badge-orange: #f2a530;
    --badge-green: #6cb84a;
  }
  * { margin: 0; padding: 0; box-sizing: border-box; }
  html, body {
    width: 1200px; height: 1200px; overflow: hidden;
    background: var(--page);
    font-family: "Montserrat", sans-serif;
  }
  .label {
    position: absolute; left: 50px; top: 160px;
    width: 1100px; height: 880px;
    border-radius: 22px; overflow: hidden;
    background: linear-gradient(160deg, var(--silver-light), var(--silver) 55%, var(--silver-light));
  }
  .top-band {
    position: absolute; left: 0; top: 0; width: 100%; height: 94px;
    background: linear-gradient(90deg, var(--brown-dark), var(--brown) 50%, var(--brown-dark));
  }
  .bottom-band {
    position: absolute; left: 0; bottom: 0; width: 100%; height: 133px;
    background: linear-gradient(90deg, var(--gold-dark), var(--gold) 35%, var(--gold-light) 70%, var(--gold));
  }
  .dot-edge {
    position: absolute; left: 0; width: 100%; height: 12px;
    background-image: radial-gradient(circle, var(--white) 3.5px, transparent 4.5px);
    background-size: 14px 12px;
  }
  .dot-edge--top { top: 88px; }
  .dot-edge--bottom { bottom: 127px; }
  .brand {
    position: absolute; left: 62px; top: 80px;
    font-weight: 800; font-size: 84px; line-height: 0.98;
    color: var(--gold);
    letter-spacing: -1px;
  }
  .product-name {
    position: absolute; left: 72px; top: 383px;
    font-weight: 800; font-size: 126px; line-height: 1;
    color: var(--ink); letter-spacing: -2px;
  }
  .product-type {
    position: absolute; left: 76px; top: 536px;
    width: 589px; height: 117px;
    background: linear-gradient(90deg, var(--gold-dark), var(--gold) 50%, var(--gold-light));
    color: var(--white);
    font-weight: 800; font-size: 100px; line-height: 117px;
    text-align: center; letter-spacing: 1px;
  }
  .net-weight {
    position: absolute; left: 76px; top: 686px;
    font-weight: 400; font-size: 44px; line-height: 1; color: var(--ink);
    letter-spacing: 3px;
  }
  .ribbon {
    position: absolute; left: 800px; top: 0;
    width: 173px; height: 662px;
  }
  .badge {
    position: absolute; left: 829px;
    width: 114px; height: 114px; border-radius: 50%;
    border: 6px solid var(--white);
  }
  .badge--gluten-free { top: 147px; background: var(--badge-orange); }
  .badge--natural { top: 297px; background: var(--badge-green); }
  .badge--vegan { top: 442px; background: var(--badge-green); }
</style>
</head>
<body>
  <div class="label">
    <div class="top-band"></div>
    <div class="dot-edge dot-edge--top"></div>

    <div class="brand">Velvet<br>Orchard</div>

    <div class="product-name">ALMOND</div>
    <div class="product-type">BUTTER</div>
    <div class="net-weight">180 G</div>

    <svg class="ribbon" viewBox="0 0 173 662" aria-hidden="true">
      <defs>
        <linearGradient id="ribbonFill" x1="0" x2="1">
          <stop offset="0" stop-color="#2f1a0c"/>
          <stop offset="0.5" stop-color="#4f2e15"/>
          <stop offset="1" stop-color="#2f1a0c"/>
        </linearGradient>
      </defs>
      <polygon points="0,0 173,0 173,626 86.5,662 0,626" fill="url(#ribbonFill)"/>
    </svg>
    <div class="badge badge--gluten-free" role="img" aria-label="Gluten free badge"></div>
    <div class="badge badge--natural" role="img" aria-label="100% natural badge"></div>
    <div class="badge badge--vegan" role="img" aria-label="Vegan badge"></div>

    <div class="dot-edge dot-edge--bottom"></div>
    <div class="bottom-band"></div>
  </div>
</body>
</html>
```